Business Card Design

I need a business card for my corporation. We are a fast food Mexican Taqueria located in San Jose, CA. I want the cards to include our business logo. The cards need to be simple but elegant. Our theme through out our locations is a beach feel atmosphere. I would like to see cards with a beach feeling. Our website is tacosdelpuerto.net and it would be great if the cards matched our website.

Industry/Entity Type

Business

Contact Information for Business Card

Monica Ferrer, VP
2637 Birch Hollow Ave
San Jose, CA 95116
Direct: 4085527319

```html
<!DOCTYPE html>
<html lang="en">
<head>
<meta charset="utf-8">
<title>Puerto Sol Business Card</title>
<link rel="stylesheet" href="https://fonts.googleapis.com/css2?family=Open+Sans:wght@600;700&display=swap">
<style>
  :root {
    --backdrop: #dcd9d5;
    --card-paper: #eeeff0;
    --brand-red: #c0262d;
    --stripe-grey: #a9a9ab;
    --sun-yellow: #f2c81e;
    --ink: #111111;
  }
  html, body {
    margin: 0;
    padding: 0;
    width: 1200px;
    height: 1111px;
    overflow: hidden;
    background: var(--backdrop);
  }
  .canvas {
    position: relative;
    width: 1200px;
    height: 1111px;
  }
  .business-card {
    position: absolute;
    left: 100px;
    top: 263px;
    width: 1000px;
    height: 585px;
    background: var(--card-paper);
    overflow: hidden;
    box-shadow: 0 6px 18px rgba(0, 0, 0, 0.18);
    font-family: "Open Sans", Arial, sans-serif;
  }
  .card-stripes {
    position: absolute;
    inset: 0;
  }
  .brand {
    position: absolute;
    left: 136px;
    top: 128px;
    display: flex;
    align-items: center;
    gap: 14px;
  }
  .brand-mark {
    width: 26px;
    height: 26px;
    border-radius: 50%;
    background: var(--sun-yellow);
  }
  .brand-name {
    margin: 0;
    font-size: 62px;
    font-weight: 700;
    color: var(--brand-red);
    line-height: 1;
  }
  .contact-line {
    position: absolute;
    left: 548px;
    top: 450px;
    margin: 0;
    font-size: 36px;
    font-weight: 700;
    color: var(--ink);
    white-space: nowrap;
  }
  .contact-label {
    color: var(--brand-red);
  }
</style>
</head>
<body>
<main class="canvas">
  <section class="business-card">
    <svg class="card-stripes" width="1000" height="585" viewBox="0 0 1000 585" aria-hidden="true">
      <line x1="158" y1="590" x2="1004" y2="150" stroke="var(--stripe-grey)" stroke-width="8"/>
      <line x1="142" y1="590" x2="1004" y2="138" stroke="var(--brand-red)" stroke-width="8"/>
    </svg>
    <div class="brand">
      <h1 class="brand-name">Puerto Sol</h1>
      <span class="brand-mark"></span>
    </div>
    <p class="contact-line"><span class="contact-label">Direct:</span> 4085527319</p>
  </section>
</main>
</body>
</html>
```